Home page and features page design for SaaS company

We're looking for designs for a home page and a features page of a new website (possibly more pages to be commissioned thereafter). The website is called 'Plainly Afloat' and is a service that helps swimming clubs and schools reduce administration.

The website will have a clean, minimalist, modern feel but not corporate. Here's an idea of the type of style: https://rostrik.net/pages/payments

At the top of the home page (above the fold) will show the two personas that the website is targeting (Swimming clubs and Swimming Schools) on a styled background (no cheesy stock images please!). Those personas can be represented as an illustration (see page 2 for an example), line art graphic or icon and will link through to a features page.

For your information, the type of people that are members of swimming clubs include beginners, competitive squads and adult swimmers. People that attend a swimming school are typically children learning to swim. If you can represent the above in simple line art illustrations/graphics/icons that match the style of our logo - great!

Below the fold on the home page will be an illustration of the main functions of the site (with our logo central to that) and at the bottom of the page will be what they get for free, testimonials and a call to action for booking a demo.

I've attached a simple wireframe of the home page for your information.

The second page is the features page. This summarises the benefits of each major feature. Each feature listed on the page is separated by a call to action. Here's a link to the content of the features page: http://webnode4.quillar-advisory.com/KTRmarketingpages/swimming/swim-club-management-software.html

Don't take a lead from the look / feel / design of this page. I don't like it (hence I'm on here to find a better design!). One thing I'd like to incorporate is a snippet preview of a screenshot on the features page (a bit like in the example). The user can click on this and the full screenshot will load in a pop-up.

The style of the features page should flow from the home page.
Updates

Project Deadline Extended
Reason: Extending deadline to allow more quality designs and give those that have submitted time to make any revisions.

Target Market(s)

Swimming clubs and swimming schools

Industry/Entity Type

Internet

Number of Pages Required

2 page

Font styles to use
Sans Serif

Colors
33a6d7
33b8a4

Requirements
Must have
• Clean, minimalist, modern feel but not corporate. Here's an idea of the type of style: https://rostrik.net/pages/payments
Should not have
• Unstylised stock photographs

```html
<!DOCTYPE html>
<html lang="en">
<head>
<meta charset="utf-8">
<title>Plainly Afloat – Membership software for swimming clubs and schools</title>
<link href="https://fonts.googleapis.com/css2?family=Roboto:wght@300;400;500;700&display=swap" rel="stylesheet">
<style>
:root{
  --nav:#1e2833;
  --blue:#33a6d7;
  --blue-deep:#1f6fc0;
  --teal:#33b8a4;
  --teal-bright:#1fd4b8;
  --ink:#2c3440;
  --muted:#7c8794;
  --panel:#eef0f4;
  --band:#b7c6d3;
  --footer:#e6eaf0;
  --white:#ffffff;
}
*{box-sizing:border-box;margin:0;padding:0}
html,body{width:1200px;height:2500px;overflow:hidden}
body{font-family:'Roboto',Arial,sans-serif;color:var(--ink);background:var(--white)}

/* header */
.site-header{height:80px;background:var(--nav);display:flex;align-items:center;padding:0 40px}
.brand{display:flex;align-items:center;gap:10px;font-size:22px;font-weight:700;color:var(--blue)}
.brand-dot{width:18px;height:18px;border-radius:50%;background:var(--blue)}
.main-nav{margin-left:auto;display:flex;gap:34px}
.main-nav a{color:var(--white);text-decoration:none;font-size:15px;font-weight:500}
.signup{margin-left:60px;border:2px solid var(--teal-bright);color:var(--teal-bright);font-size:13px;font-weight:700;padding:8px 22px;border-radius:3px;text-transform:uppercase}

/* hero */
.hero{height:380px;background:linear-gradient(180deg,var(--blue-deep) 0%,var(--blue) 100%);text-align:center;color:var(--white);padding-top:46px}
.hero h1{font-size:34px;font-weight:700}
.personas{display:flex;justify-content:center;gap:200px;margin-top:40px}
.persona{display:flex;flex-direction:column;align-items:center}
.persona-art{width:140px;height:120px;border-radius:20px;background:linear-gradient(180deg,#7fd2ee,#2e8fd0)}
.persona h2{font-size:24px;font-weight:500;margin-top:18px}
.btn-outline{margin-top:12px;border:2px solid var(--white);padding:8px 22px;font-size:14px;font-weight:700;letter-spacing:.5px;border-radius:3px}

/* functions diagram */
.functions{height:440px;position:relative}
.functions .section-icon{position:absolute;left:582px;top:20px}
.hub{position:absolute;left:430px;top:150px;width:340px;height:200px;border-radius:120px 140px 90px 90px;background:linear-gradient(180deg,#57b8ea,#2679c8)}
.node{position:absolute;display:flex;align-items:center;gap:10px;font-size:13px;color:var(--muted)}
.node i{width:26px;height:26px;border-radius:50%;background:var(--teal-bright);display:block;flex:none}
.spoke{position:absolute;height:2px;background:#c6d4de;transform-origin:left center}

/* free benefits */
.benefits{display:grid;grid-template-columns:340px 340px;gap:60px 80px;justify-content:center;margin-top:40px}
.benefit{background:var(--panel);padding:30px 30px 28px;position:relative;min-height:130px}
.benefit-icon{position:absolute;right:-14px;top:-26px;width:56px;height:56px;background:var(--teal-bright);display:flex;align-items:center;justify-content:center}
.benefit h3{font-size:16px;font-weight:700;text-transform:uppercase;margin-bottom:12px}
.benefit p{font-size:13px;line-height:1.55;color:var(--muted);max-width:240px}

/* testimonials */
.testimonials-head{display:flex;justify-content:center;align-items:center;gap:50px;margin-top:100px;font-size:22px;font-weight:500}
.testimonials-head .rule{width:120px;height:2px;background:#d6dde4}
.cards{display:flex;justify-content:center;gap:40px;margin-top:60px}
.card{width:320px;border:1px solid #e2e7ec;padding:24px;box-shadow:0 4px 14px rgba(0,0,0,.05)}
.stars{color:var(--teal);font-size:16px;letter-spacing:3px}
.card p{font-size:13px;line-height:1.55;color:var(--muted);margin-top:10px}
.person{display:flex;align-items:center;gap:12px;margin-top:22px}
.avatar{width:40px;height:40px;border-radius:50%;background:#b8c2cc}
.person b{font-size:14px;display:block}
.person span{font-size:12px;color:var(--muted)}

/* demo band */
.demo{position:absolute;top:1820px;left:0;width:1200px;height:260px;background:var(--band);text-align:center;padding-top:70px}
.demo h2{font-size:42px;font-weight:500;color:var(--ink)}
.btn-teal{display:inline-block;margin-top:26px;background:var(--teal-bright);color:var(--white);font-size:14px;font-weight:700;padding:12px 28px;border-radius:3px}

/* subscribe */
.subscribe{position:absolute;top:2080px;left:0;width:1200px;height:220px;background:var(--teal-bright);text-align:center;color:var(--white);padding-top:34px}
.subscribe h2{font-size:20px;font-weight:700;margin-top:8px;letter-spacing:1px}
.subscribe p{font-size:13px;margin-top:10px}
.sub-form{display:flex;justify-content:center;margin-top:18px}
.sub-form .field{width:320px;height:40px;background:var(--white);color:var(--muted);font-size:13px;text-align:left;padding:12px 14px}
.sub-form .go{height:40px;background:var(--nav);font-size:13px;font-weight:700;padding:12px 26px}
.subscribe small{display:block;font-size:11px;margin-top:12px;opacity:.85}

/* footer */
.site-footer{position:absolute;top:2300px;left:0;width:1200px;height:200px;background:var(--footer);text-align:center;padding-top:50px}
.site-footer .brand{justify-content:center;font-size:30px}
.site-footer p{font-size:13px;color:var(--muted);margin-top:12px}
</style>
</head>
<body>

<header class="site-header">
  <div class="brand"><span class="brand-dot"></span>Plainly Afloat</div>
  <nav class="main-nav">
    <a href="#">About us</a><a href="#">Pricing</a><a href="#">Free resources</a><a href="#">Free account</a><a href="#">Contact us</a>
  </nav>
  <div class="signup">Sign up</div>
</header>

<section class="hero">
  <h1>Membership software for swimming clubs and schools</h1>
  <div class="personas">
    <div class="persona">
      <div class="persona-art" role="img" aria-label="Illustration of a fish in a bowl representing swimming clubs"></div>
      <h2>Swimming Clubs</h2>
      <div class="btn-outline">FIND OUT MORE</div>
    </div>
    <div class="persona">
      <div class="persona-art" role="img" aria-label="Illustration of a lifeguard chair representing swimming schools"></div>
      <h2>Swimming Schools</h2>
      <div class="btn-outline">FIND OUT MORE</div>
    </div>
  </div>
</section>

<section class="functions">
  <svg class="section-icon" width="36" height="36" viewBox="0 0 36 36" fill="none" stroke="#33b8a4" stroke-width="2.5"><path d="M18 4 32 11 18 18 4 11Z"/><path d="M4 18l14 7 14-7"/><path d="M4 25l14 7 14-7"/></svg>
  <div class="spoke" style="left:600px;top:250px;width:110px;transform:rotate(-90deg)"></div>
  <div class="spoke" style="left:600px;top:250px;width:210px;transform:rotate(-28deg)"></div>
  <div class="spoke" style="left:600px;top:250px;width:200px;transform:rotate(210deg)"></div>
  <div class="spoke" style="left:600px;top:250px;width:200px;transform:rotate(172deg)"></div>
  <div class="spoke" style="left:600px;top:250px;width:210px;transform:rotate(12deg)"></div>
  <div class="hub" role="img" aria-label="Cloud illustration with a swimmer at the centre of the platform's functions"></div>
  <div class="node" style="left:560px;top:110px;flex-direction:column">Online payments<i></i></div>
  <div class="node" style="left:780px;top:140px"><i></i>Membership data</div>
  <div class="node" style="left:330px;top:150px">Online registrations<i></i></div>
  <div class="node" style="left:300px;top:270px">Online payments<i></i></div>
  <div class="node" style="left:805px;top:280px"><i></i>Group email</div>
  <div class="node" style="left:550px;top:360px;flex-direction:column"><i></i>Class management</div>
</section>

<section class="benefits">
  <div class="benefit">
    <div class="benefit-icon"><svg width="26" height="26" viewBox="0 0 26 26" fill="none" stroke="#fff" stroke-width="2"><path d="M4 22 14 12M10 6l10 10M16 4l6 6-4 4-6-6Z"/></svg></div>
    <h3>Access to exclusive tools</h3>
    <p>We have over 150 great features and functions to help cut down admin and increase payment collection.</p>
  </div>
  <div class="benefit">
    <div class="benefit-icon"><svg width="26" height="26" viewBox="0 0 26 26" fill="none" stroke="#fff" stroke-width="2"><path d="M7 4h12v6a6 6 0 0 1-12 0Z"/><path d="M13 16v5M8 22h10"/></svg></div>
    <h3>Account setup</h3>
    <p>We take time to understand how your club works and set your account up to maximise efficiencies.</p>
  </div>
  <div class="benefit">
    <div class="benefit-icon"><svg width="26" height="26" viewBox="0 0 26 26" fill="none" stroke="#fff" stroke-width="2"><path d="M6 20 18 8l2 2L8 22H6Z"/><path d="M16 6l4 4"/></svg></div>
    <h3>Software updates</h3>
    <p>We continuously listen to our clients and develop functionality in the cloud. Direct feedback to help you improve efficiencies and save time.</p>
  </div>
  <div class="benefit">
    <div class="benefit-icon"><svg width="26" height="26" viewBox="0 0 26 26" fill="none" stroke="#fff" stroke-width="2"><path d="M7 4v18M13 4v18M19 4v18"/><path d="M4 9h6M10 16h6M16 11h6"/></svg></div>
    <h3>First class support</h3>
    <p>From your first booking session to on-going support, we're here to help you get the best from the system. You can reach us by live chat, email or phone.</p>
  </div>
</section>

<div class="testimonials-head">
  <span>What our Customers</span>
  <svg width="40" height="34" viewBox="0 0 40 34" fill="none" stroke="#33b8a4" stroke-width="2.5"><path d="M4 4h24v16H14l-6 6v-6H4Z"/><path d="M32 10h4v14h-4v6l-6-6H16"/></svg>
  <span>Says about Plainly Afloat</span>
</div>

<section class="cards">
  <article class="card">
    <div class="stars">★★★★★</div>
    <p>Plainly Afloat has saved our club hours every week. Payments arrive on time and our volunteers finally have their evenings back.</p>
    <div class="person"><div class="avatar"></div><div><b>Nora Pelling</b><span>Club Secretary</span></div></div>
  </article>
  <article class="card">
    <div class="stars">★★★★★</div>
    <p>Registering swimmers used to be a paper chase. Now parents sign up online and our coaches see every squad list instantly.</p>
    <div class="person"><div class="avatar"></div><div><b>Ivy Carrow</b><span>Head Coach</span></div></div>
  </article>
  <article class="card">
    <div class="stars">★★★★★</div>
    <p>Our swim school runs smoother than ever. Class bookings, reminders and payments all happen in one place without extra work.</p>
    <div class="person"><div class="avatar"></div><div><b>Tessa Mirren</b><span>School Owner</span></div></div>
  </article>
</section>

<section class="demo">
  <h2>Book a FREE demo now</h2>
  <div class="btn-teal">▶ TRY IT NOW</div>
</section>

<section class="subscribe">
  <svg width="34" height="26" viewBox="0 0 34 26" fill="none" stroke="#fff" stroke-width="2.5"><rect x="2" y="2" width="30" height="22"/><path d="M2 2l15 12L32 2"/></svg>
  <h2>SUBSCRIBE</h2>
  <p>Subscribe to our newsletter and stay up to date with helpful tips and news.</p>
  <div class="sub-form"><div class="field">Enter your email address</div><div class="go">SUBMIT</div></div>
  <small>We respect your privacy. Unsubscribe at any time.</small>
</section>

<footer class="site-footer">
  <div class="brand"><span class="brand-dot"></span>Plainly Afloat</div>
  <p>Membership software for clubs and schools</p>
  <p>© 2024 Plainly Afloat. All rights reserved.</p>
</footer>

</body>
</html>
```